Wren Vehicle Polishing (Mobile detail)

I need a business card made up. I'd like it to be different in some form, either raised, embossed, debossed, something cool that stands out. (preferably embossed text somewhere in it). I will be including the Initial png file. Let me know if you need the photoshop of adobe illustrator file to work with.
Updates

Information to be included: Text: XXX-XXX-XXXX Phone: XXX-XXX-XXXX Email: wrenvehiclepolish@mailnest.example Website: www.socialpage.example/wrenvehiclepolishKTR Hours of operation: Mon - Fri 7:00AM to 8:00PM Sat - 10:00AM to 8:00PM

Target Market(s)

Mobile automotive detailing

Industry/Entity Type

Automotive

Contact Information for Business Card

Make it stand out with embossed lettering, I'd also like the background to be glossy black or matte, something that represents a shiny car, black preferred

Requirements
Must have
• A glossy background, or something.
• My logo, pick one of them that best fits your design.
Should not have
• White background,
• something that does not stand out.

```html
<!DOCTYPE html>
<html lang="en">
<head>
<meta charset="utf-8">
<title>Wren Vehicle Polishing — Business Card</title>
<link href="https://fonts.googleapis.com/css2?family=Orbitron:wght@800&family=Open+Sans:wght@400;600&display=swap" rel="stylesheet">
<style>
  :root {
    --stage: #b9b9b9;
    --panel-dark: #232425;
    --panel-dark-edge: #2e3032;
    --orange-deep: #c9361a;
    --orange-mid: #e0501f;
    --orange-light: #f07a3c;
    --silver: #d9dcdf;
    --silver-shade: #8d9196;
    --ink: #111111;
    --ink-soft: #2a1208;
    --paper-text: #fff4ec;
  }
  * { margin: 0; padding: 0; box-sizing: border-box; }
  html, body {
    width: 1200px; height: 900px; overflow: hidden;
    background: var(--stage);
  }
  .business-card {
    position: absolute; left: 100px; top: 165px;
    width: 1000px; height: 571px;
    overflow: hidden;
    box-shadow: 0 6px 18px rgba(0,0,0,.35);
  }
  .card-background { position: absolute; inset: 0; }
  .brand-lockup {
    position: absolute; left: 60px; top: 210px; width: 360px;
    display: flex; align-items: center; gap: 16px;
  }
  .brand-mark {
    flex: none; width: 54px; height: 54px; border-radius: 50%;
    background: var(--orange-mid);
  }
  .brand-name {
    font-family: "Open Sans", sans-serif; font-weight: 600;
    font-size: 36px; line-height: 1.15; color: var(--silver);
  }
  .contact-block {
    position: absolute; right: 44px; top: 62px; width: 520px;
    text-align: right; font-family: "Open Sans", sans-serif;
  }
  .holder-name {
    font-family: "Orbitron", sans-serif; font-weight: 800;
    font-size: 30px; letter-spacing: 1px; color: var(--ink);
  }
  .holder-role {
    font-size: 19px; color: var(--paper-text); margin-top: 4px; margin-right: 40px;
  }
  .contact-list { list-style: none; margin-top: 38px; }
  .contact-item {
    display: flex; justify-content: flex-end; align-items: center; gap: 12px;
    font-size: 19px; color: var(--paper-text); line-height: 1.75;
  }
  .contact-icon { width: 18px; height: 18px; flex: none; }
  .hours { margin-top: 26px; margin-right: 30px; }
  .hours-title { font-size: 21px; font-weight: 600; color: var(--ink); }
  .hours-line { font-size: 20px; color: var(--paper-text); line-height: 1.6; }
</style>
</head>
<body>
  <section class="business-card">
    <svg class="card-background" viewBox="0 0 1000 571" width="1000" height="571" aria-hidden="true">
      <defs>
        <radialGradient id="orangeGlow" cx="0.42" cy="0.35" r="0.8">
          <stop offset="0" stop-color="var(--orange-light)"/>
          <stop offset="0.45" stop-color="var(--orange-mid)"/>
          <stop offset="1" stop-color="var(--orange-deep)"/>
        </radialGradient>
        <linearGradient id="darkPanel" x1="0" y1="0" x2="1" y2="1">
          <stop offset="0" stop-color="var(--panel-dark-edge)"/>
          <stop offset="1" stop-color="var(--panel-dark)"/>
        </linearGradient>
        <linearGradient id="silverEdge" x1="0" y1="0" x2="0" y2="1">
          <stop offset="0" stop-color="var(--silver-shade)"/>
          <stop offset="0.4" stop-color="var(--silver)"/>
          <stop offset="1" stop-color="var(--silver-shade)"/>
        </linearGradient>
      </defs>
      <rect width="1000" height="571" fill="url(#orangeGlow)"/>
      <path d="M0,0 L545,0 C505,55 470,125 505,200 C540,285 470,370 360,430 C250,485 120,505 0,560 Z"
            fill="url(#silverEdge)"/>
      <path d="M0,0 L525,0 C485,55 452,125 487,200 C518,280 452,360 345,416 C240,468 115,488 0,540 Z"
            fill="url(#darkPanel)"/>
    </svg>

    <div class="brand-lockup">
      <span class="brand-mark"></span>
      <span class="brand-name">Wren Vehicle Polishing</span>
    </div>

    <div class="contact-block">
      <h1 class="holder-name">DANA MARSH</h1>
      <p class="holder-role">Director</p>
      <ul class="contact-list">
        <li class="contact-item">XXX-XXX-XXXX
          <svg class="contact-icon" viewBox="0 0 18 18"><rect x="5" y="1" width="8" height="16" rx="1.5" fill="none" stroke="#111" stroke-width="1.8"/><rect x="8" y="14" width="2" height="1.5" fill="#111"/></svg>
        </li>
        <li class="contact-item">XXX-XXX-XXXX
          <svg class="contact-icon" viewBox="0 0 18 18"><path d="M2,7 C2,3 16,3 16,7 L13,8 L12,6 L6,6 L5,8 Z" fill="#111"/><rect x="4" y="9" width="10" height="7" rx="1" fill="#111"/></svg>
        </li>
        <li class="contact-item">wrenvehiclepolish@mailnest.example
          <svg class="contact-icon" viewBox="0 0 18 18"><rect x="1" y="4" width="16" height="11" fill="#111"/><path d="M1,4 L9,10 L17,4" fill="none" stroke="#f07a3c" stroke-width="1.2"/></svg>
        </li>
        <li class="contact-item">/wrenvehiclepolishKTR
          <svg class="contact-icon" viewBox="0 0 18 18"><rect x="2" y="2" width="14" height="14" rx="2" fill="#111"/></svg>
        </li>
      </ul>
      <div class="hours">
        <p class="hours-title">Hours of operation</p>
        <p class="hours-line">Mon - Fri 7:00AM to 8:00PM</p>
        <p class="hours-line">Sat - 10:00AM to 8:00PM</p>
      </div>
    </div>
  </section>
</body>
</html>
```